Business Card;Letterhead;Folder design
Bright & Fun-filled
Teodor Mavlin
President
2783 Harlow Brook Ln
Larkfield GA 30999
855 - 4 - KOBRIX
kobrixtrans@kobrixmail.com
logos
another variation

```html
<!DOCTYPE html>
<html lang="en">
<head>
<meta charset="utf-8">
<title>Kobrix Stationery Set</title>
<link href="https://fonts.googleapis.com/css2?family=Montserrat:wght@400;600;800&display=swap" rel="stylesheet">
<style>
  :root {
    --bg: #d9bf93;
    --paper: #ffffff;
    --navy: #13306b;
    --blue: #1f4fa0;
    --blue-light: #3d78c9;
    --grey: #6f7479;
    --grey-light: #a5a9ad;
    --ink: #2b2f36;
    --label: #5a4528;
    --mark-faint: #e4ebf4;
  }
  * { margin: 0; padding: 0; box-sizing: border-box; }
  html, body { width: 1200px; height: 446px; overflow: hidden; }
  body {
    position: relative;
    background: var(--bg);
    font-family: "Montserrat", sans-serif;
    color: var(--ink);
  }
  .piece { position: absolute; background: var(--paper); box-shadow: 0 2px 6px rgba(0,0,0,.25); overflow: hidden; }
  .label {
    position: absolute; font-size: 6px; letter-spacing: .8px; white-space: nowrap;
    text-transform: uppercase; color: var(--label); font-weight: 600;
  }
  .brand { display: flex; align-items: center; gap: 4px; white-space: nowrap; }
  .brand-dot { border-radius: 50%; background: radial-gradient(circle at 40% 35%, var(--blue-light), var(--navy)); flex: none; }
  .brand-name { font-weight: 800; color: var(--navy); letter-spacing: 1px; }
  .faint-mark { position: absolute; border-radius: 50%; background: var(--mark-faint); }

  /* business cards */
  .card { width: 101px; height: 34px; }
  .card-front { left: 19px; top: 163px; }
  .card-front .brand { position: absolute; left: 8px; top: 5px; }
  .card-front .email { position: absolute; left: 8px; top: 18px; font-size: 3px; color: var(--grey); white-space: nowrap; }
  .card-front .stripe { position: absolute; left: 0; right: 0; bottom: 6px; height: 3px; background: var(--navy); }
  .card-back { left: 19px; top: 235px; }
  .card-back .brand { position: absolute; left: 8px; top: 8px; }
  .card-back .stripe { position: absolute; left: 0; right: 0; bottom: 0; height: 7px; background: var(--navy); }

  /* letterheads */
  .letterhead { width: 310px; height: 322px; top: 19px; }
  .lh-one { left: 158px; }
  .lh-one .brand { position: absolute; left: 16px; top: 14px; }
  .lh-one .contact { position: absolute; right: 16px; top: 14px; font-size: 3.4px; line-height: 5.2px; color: var(--grey); white-space: nowrap; }
  .lh-one .faint-mark { width: 118px; height: 118px; left: 172px; top: 196px; }
  .lh-two { left: 477px; }
  .lh-two .brand { position: absolute; left: 50%; top: 14px; transform: translateX(-50%); }
  .lh-two .faint-mark { width: 130px; height: 130px; left: 82px; top: 118px; }
  .lh-two .footer-band {
    position: absolute; left: 0; right: 0; bottom: 0; height: 16px;
    background: linear-gradient(var(--blue), var(--navy));
    color: #dbe6f7; font-size: 3.4px; display: flex; align-items: center; justify-content: center; gap: 10px; white-space: nowrap;
  }

  /* envelopes */
  .env-blue { left: 840px; top: 7px; width: 331px; height: 65px; background: linear-gradient(var(--blue-light), var(--navy)); }
  .env-grey-open { left: 816px; top: 91px; width: 360px; height: 156px; background: transparent; }
  .env-plain { left: 792px; top: 259px; width: 350px; height: 160px; }
  .env-plain .brand { position: absolute; left: 16px; top: 14px; }
  .env-plain .stripe { position: absolute; left: 0; right: 0; bottom: 0; height: 8px; background: var(--navy); }
</style>
</head>
<body>

  <div class="label" style="left:19px; top:124px;">Background Concepts</div>

  <section class="piece card card-front">
    <div class="brand"><span class="brand-dot" style="width:8px;height:8px"></span><span class="brand-name" style="font-size:6.5px">KOBRIX</span></div>
    <div class="email">kobrixtrans@kobrixmail.com</div>
    <div class="stripe"></div>
  </section>
  <div class="label" style="left:19px; top:203px;">Business Card Front</div>

  <section class="piece card card-back">
    <div class="brand"><span class="brand-dot" style="width:8px;height:8px"></span><span class="brand-name" style="font-size:6.5px">KOBRIX</span></div>
    <div class="stripe"></div>
  </section>
  <div class="label" style="left:19px; top:275px;">Business Card Back</div>

  <section class="piece letterhead lh-one">
    <div class="brand"><span class="brand-dot" style="width:14px;height:14px"></span><span class="brand-name" style="font-size:11px">KOBRIX</span></div>
    <div class="contact">
      2783 Harlow Brook Ln<br>Larkfield GA 30999<br>855 - 4 - KOBRIX<br>kobrixtrans@kobrixmail.com
    </div>
    <div class="faint-mark" role="img" aria-label="Faint brand watermark"></div>
  </section>
  <div class="label" style="left:270px; top:354px;">Letterhead Option 1</div>

  <section class="piece letterhead lh-two">
    <div class="brand"><span class="brand-dot" style="width:14px;height:14px"></span><span class="brand-name" style="font-size:11px">KOBRIX</span></div>
    <div class="faint-mark" role="img" aria-label="Faint brand watermark"></div>
    <div class="footer-band"><span>2783 Harlow Brook Ln, Larkfield GA 30999</span><span>855 - 4 - KOBRIX</span></div>
  </section>
  <div class="label" style="left:590px; top:354px;">Letterhead Option 2</div>

  <section class="piece env-blue"></section>

  <svg class="piece env-grey-open" viewBox="0 0 360 156" aria-hidden="true">
    <defs>
      <linearGradient id="greyFlap" x1="0" y1="0" x2="0" y2="1">
        <stop offset="0" stop-color="#a5a9ad"/><stop offset="1" stop-color="#6f7479"/>
      </linearGradient>
      <radialGradient id="seal" cx=".4" cy=".35"><stop offset="0" stop-color="#3d78c9"/><stop offset="1" stop-color="#13306b"/></radialGradient>
    </defs>
    <rect x="0" y="0" width="360" height="156" fill="#ffffff"/>
    <path d="M0 22 L180 120 L360 22 Z" fill="#f1f2f4" stroke="#d6d8db" stroke-width="1"/>
    <path d="M0 0 H360 V22 Q180 90 0 22 Z" fill="url(#greyFlap)"/>
    <circle cx="180" cy="96" r="13" fill="url(#seal)"/>
  </svg>

  <section class="piece env-plain">
    <div class="brand"><span class="brand-dot" style="width:10px;height:10px"></span><span class="brand-name" style="font-size:8px">KOBRIX</span></div>
    <div class="stripe"></div>
  </section>
  <div class="label" style="left:925px; top:427px;">Envelope Options</div>

</body>
</html>
```